Graphical design for food product in 1 Liter carton

We need this design not for a real product but as a showcase for a new service.

This special situation makes it really simple for you to participate because you only have to care about how the visual impression of your design is.

Furthermore it gives you the opportunity to get an extra winning chance if you choose to also participate in the open competition at our website - where you can enter the same design as you enter here at ArtQuarry.

Here is the requirements:

1. You must apply your design to our attatched template

2. Make a design for a food product of your own choice, which is to be sold from retail stores in a rectangular 1 L carton – based on our template.

3. You are only allowed to use brand names and/or logos that you have the rights to use for this competition, so please make completely fictive brand names and logos.

4. Your design is evaluated on the visual impression only, which means that your text on the design can be in any language and doesn’t have to relate to the design.

5. The criteria for the evaluation of your design is your creativity, the graphical quality and how well the product will display it self in the stores.

If you also want to participate in the open competition on our website - where you can win an Zelbo Slate, and will get your design skills exposed to brand owners and packaging manufacturers all over the world, then please visit plovimark.example/packaging-design-competition/

Attatched is:

A. Empty design template you must apply your design to. Remove the layer with our template when you return your send in your design.

B. Example of design applied to the template.

C. Example of the applied example design after it has been converted to 3D with our online 3D engine at PloviMark.example.

The winning design will be converted to 3D and will be used as a showcase on our website - all designers can enter their design to our open competition at PloviMark.example.

```html
<!DOCTYPE html>
<html lang="en">
<head>
<meta charset="utf-8">
<title>Zestly Orange – 1 L carton</title>
<link rel="stylesheet" href="https://fonts.googleapis.com/css2?family=Jost:wght@400;700&display=swap">
<style>
  :root {
    --red: #e0141b;
    --orange: #f5a21f;
    --yellow: #f6d52a;
    --lime: #e6f01a;
    --white: #ffffff;
    --black: #0a0a0a;
    --slice: #f28a12;
    --slice-light: #fbb64a;
  }
  html, body {
    margin: 0;
    padding: 0;
    width: 1200px;
    height: 1066px;
    overflow: hidden;
    background: var(--white);
  }
  .carton {
    position: relative;
    width: 1200px;
    height: 1066px;
    overflow: hidden;
    font-family: "Jost", sans-serif;
  }
  .panel {
    position: absolute;
    top: 0;
    height: 1066px;
  }
  .panel--front { background: linear-gradient(to bottom, var(--red) 0%, #ee5a22 14%, var(--orange) 30%, var(--yellow) 58%, var(--lime) 100%); }
  .panel--side { background: var(--red); }
  .panel--a { left: 0; width: 306px; }
  .panel--b { left: 306px; width: 298px; }
  .panel--c { left: 604px; width: 299px; }
  .panel--d { left: 903px; width: 297px; }

  .glow {
    position: absolute;
    width: 340px;
    height: 340px;
    border-radius: 50%;
    background: radial-gradient(circle, rgba(255,255,255,0.95) 0%, rgba(255,255,255,0.6) 35%, rgba(255,255,255,0) 70%);
  }
  .glow--a { left: -15px; top: 235px; }
  .glow--c { left: 585px; top: 235px; }

  .name-band {
    position: absolute;
    top: 521px;
    width: 113px;
    height: 474px;
    z-index: 3;
    background: linear-gradient(to bottom, rgba(10,10,10,0) 0%, var(--black) 7%, var(--black) 100%);
  }
  .name-band--a { left: 98px; }
  .name-band--c { left: 699px; }
  .flavour {
    display: block;
    width: 113px;
    height: 474px;
  }
  .flavour text {
    fill: var(--white);
    font-family: "Jost", sans-serif;
    font-weight: 700;
    font-size: 104px;
  }

  .bubble {
    position: absolute;
    border-radius: 50%;
    background: rgba(255,255,255,0.45);
  }

  .fruit-slice {
    position: absolute;
    border-radius: 50%;
    background: radial-gradient(circle, var(--slice-light) 0%, var(--slice) 70%, #f7c45a 92%, #fde3a0 100%);
  }
  .fruit-slice--faint {
    background: radial-gradient(circle, #ee5a3c 0%, #e8403a 80%, #e9302c 100%);
    opacity: 0.85;
  }

  .brand {
    position: absolute;
    display: flex;
    align-items: center;
    gap: 10px;
    font-weight: 700;
    line-height: 1;
  }
  .brand__dot {
    border-radius: 50%;
    background: var(--red);
  }
  .brand--main { font-size: 70px; color: var(--red); }
  .brand--main .brand__dot { width: 26px; height: 26px; }
  .brand--main.brand--a { left: 28px; top: 390px; }
  .brand--main.brand--c { left: 630px; top: 390px; }
  .brand--small { font-size: 40px; color: var(--white); }
  .brand--small .brand__dot { width: 16px; height: 16px; background: var(--white); }
  .brand--small.brand--b { left: 382px; top: 872px; }
  .brand--small.brand--d { left: 978px; top: 872px; }

  .copy {
    position: absolute;
    top: 292px;
    width: 232px;
    color: var(--white);
    font-size: 10.5px;
    line-height: 13.6px;
  }
  .copy--b { left: 338px; }
  .copy--d { left: 938px; }
  .copy p { margin: 0 0 22px; }
</style>
</head>
<body>
<div class="carton">
  <div class="panel panel--front panel--a"></div>
  <div class="panel panel--side panel--b"></div>
  <div class="panel panel--front panel--c"></div>
  <div class="panel panel--side panel--d"></div>

  <div class="fruit-slice fruit-slice--faint" role="img" aria-label="Faint orange slice photo" style="left:314px;top:338px;width:272px;height:272px;"></div>
  <div class="fruit-slice fruit-slice--faint" role="img" aria-label="Faint orange slice photo" style="left:907px;top:308px;width:272px;height:272px;"></div>

  <div class="glow glow--a"></div>
  <div class="glow glow--c"></div>

  <div class="bubble" style="left:98px;top:114px;width:76px;height:76px;"></div>
  <div class="bubble" style="left:14px;top:271px;width:54px;height:54px;"></div>
  <div class="bubble" style="left:423px;top:151px;width:54px;height:54px;"></div>
  <div class="bubble" style="left:15px;top:697px;width:52px;height:52px;"></div>
  <div class="bubble" style="left:233px;top:725px;width:138px;height:138px;"></div>
  <div class="bubble" style="left:211px;top:898px;width:76px;height:76px;"></div>
  <div class="bubble" style="left:701px;top:108px;width:78px;height:78px;"></div>
  <div class="bubble" style="left:619px;top:269px;width:54px;height:54px;"></div>
  <div class="bubble" style="left:1021px;top:157px;width:54px;height:54px;"></div>
  <div class="bubble" style="left:620px;top:699px;width:52px;height:52px;"></div>
  <div class="bubble" style="left:832px;top:749px;width:136px;height:136px;"></div>
  <div class="bubble" style="left:809px;top:880px;width:76px;height:76px;"></div>

  <div class="brand brand--main brand--a"><span class="brand__dot"></span>Zestly</div>
  <div class="brand brand--main brand--c"><span class="brand__dot"></span>Zestly</div>

  <div class="copy copy--b">
    <p>Squeezed from sun ripened oranges picked at the peak of the season, every carton holds pure juice with no added sugar, no water and no preservatives. Bright, tangy and full of natural vitamin C, it is the easy way to start each morning with a glass of real fruit. Shake well before serving and enjoy it cold.</p>
    <p>Ingredients: one hundred percent orange juice from fresh fruit. Pasteurised for safety and packed in a recyclable carton to keep flavour locked in until you open it. Each serving gives you a bright boost of fruit goodness.</p>
    <p>Store in a cool dry place. Once opened, keep chilled and drink within five days. Best before date shown on top.</p>
  </div>
  <div class="copy copy--d">
    <p>Squeezed from sun ripened oranges picked at the peak of the season, every carton holds pure juice with no added sugar, no water and no preservatives. Bright, tangy and full of natural vitamin C, it is the easy way to start each morning with a glass of real fruit. Shake well before serving and enjoy it cold.</p>
    <p>Ingredients: one hundred percent orange juice from fresh fruit. Pasteurised for safety and packed in a recyclable carton to keep flavour locked in until you open it. Each serving gives you a bright boost of fruit goodness.</p>
    <p>Store in a cool dry place. Once opened, keep chilled and drink within five days. Best before date shown on top.</p>
  </div>

  <div class="brand brand--small brand--b"><span class="brand__dot"></span>Zestly</div>
  <div class="brand brand--small brand--d"><span class="brand__dot"></span>Zestly</div>

  <div class="fruit-slice" role="img" aria-label="Orange slice photo" style="left:-5px;top:950px;width:240px;height:240px;"></div>
  <div class="fruit-slice" role="img" aria-label="Orange slice photo" style="left:222px;top:955px;width:240px;height:240px;"></div>
  <div class="fruit-slice" role="img" aria-label="Orange slice photo" style="left:455px;top:952px;width:240px;height:240px;"></div>
  <div class="fruit-slice" role="img" aria-label="Orange slice photo" style="left:695px;top:950px;width:240px;height:240px;"></div>
  <div class="fruit-slice" role="img" aria-label="Orange slice photo" style="left:935px;top:955px;width:240px;height:240px;"></div>

  <div class="name-band name-band--a">
    <svg class="flavour" viewBox="0 0 113 474" aria-label="ORANGE"><text transform="translate(94 462) rotate(-90)" textLength="424" lengthAdjust="spacingAndGlyphs">ORANGE</text></svg>
  </div>
  <div class="name-band name-band--c">
    <svg class="flavour" viewBox="0 0 113 474" aria-label="ORANGE"><text transform="translate(94 462) rotate(-90)" textLength="424" lengthAdjust="spacingAndGlyphs">ORANGE</text></svg>
  </div>
</div>
</body>
</html>
```